Korvane Sky Works, LLC - Business Card

I currently have a drone business that specializes in aerial photography, thermal image inspections, deer recovery, search and rescue, custom agricultural applications. i will attach my current business card as well as some logos to incorporate for a new up to date business card
Updates

Designs look the same

Sick

Target Market(s)

farmers, hunters

Contact Information for Business Card

name address phone number (as existing card i attached)

Requirements
Must have
• im good with existing business card, but would like an agricultural twist

```html
<!DOCTYPE html>
<html lang="en">
<head>
<meta charset="utf-8">
<title>Korvane Sky Works, LLC – Business Card</title>
<link rel="stylesheet" href="https://fonts.googleapis.com/css2?family=Montserrat:wght@400;500;700;800&display=swap">
<style>
  :root {
    --stage: #1d1d1d;
    --field-green: #278040;
    --leaf-green: #62a544;
    --accent-green: #3f9b3c;
    --charcoal: #333333;
    --paper: #ffffff;
    --ink: #2b2b2b;
  }
  * { margin: 0; padding: 0; box-sizing: border-box; }
  html, body {
    width: 1200px; height: 1015px; overflow: hidden;
    background: var(--stage);
    font-family: "Montserrat", sans-serif;
  }
  .card {
    position: absolute; left: 300px;
    width: 600px; height: 343px;
    overflow: hidden;
    box-shadow: 0 10px 30px rgba(0,0,0,.5);
  }
  /* Front */
  .card-front { top: 105px; background: var(--field-green); }
  .front-mark {
    position: absolute; left: 50%; top: 50%;
    transform: translate(-50%, -50%);
    display: flex; align-items: center; gap: 16px;
  }
  .mark-dot {
    width: 54px; height: 54px; border-radius: 50%;
    border: 5px solid var(--paper);
  }
  .front-name {
    color: var(--paper); font-weight: 800; font-size: 34px;
    letter-spacing: 1px; text-transform: uppercase; line-height: 1.05;
  }
  /* Back */
  .card-back { top: 567px; background: var(--paper); }
  .green-band {
    position: absolute; right: 0; top: 58px;
    width: 190px; height: 95px; background: var(--leaf-green);
  }
  .contact-band {
    position: absolute; left: 0; top: 118px;
    width: 410px; height: 132px; background: var(--charcoal);
  }
  .identity {
    position: absolute; left: 0; top: 56px;
    padding-left: 34px; border-left: 12px solid var(--accent-green);
  }
  .person-name {
    color: var(--accent-green); font-weight: 800; font-size: 27px;
    letter-spacing: 1px; line-height: 1;
  }
  .person-role { color: var(--ink); font-size: 14px; margin-top: 4px; }
  .contact-list {
    position: absolute; left: 40px; top: 128px;
    list-style: none; color: var(--paper); font-size: 13px;
  }
  .contact-list li { display: flex; align-items: center; gap: 12px; margin-bottom: 5px; line-height: 1.2; }
  .contact-list li:first-child { margin-bottom: 7px; }
  .contact-list li:last-child { margin-bottom: 0; }
  .icon {
    width: 22px; height: 22px; flex: none; border-radius: 50%;
    background: var(--paper); border: 3px solid var(--accent-green);
    display: flex; align-items: center; justify-content: center;
  }
  .icon svg { width: 11px; height: 11px; }
  .service-list {
    position: absolute; left: 68px; top: 258px;
    list-style: none; color: var(--ink); font-size: 14px; line-height: 1.3;
  }
  .service-list li::before {
    content: ""; display: inline-block; width: 7px; height: 7px;
    border-radius: 50%; background: var(--accent-green);
    margin-right: 10px; vertical-align: middle;
  }
  .back-mark {
    position: absolute; left: 352px; top: 60px;
    width: 180px; height: 180px; border-radius: 50%;
    background: var(--paper); border: 7px solid var(--accent-green);
    display: flex; align-items: center; justify-content: center; text-align: center;
  }
  .back-name {
    color: var(--accent-green); font-weight: 800; font-size: 22px;
    text-transform: uppercase; line-height: 1.1;
  }
</style>
</head>
<body>
  <section class="card card-front">
    <div class="front-mark">
      <span class="mark-dot"></span>
      <span class="front-name">Korvane<br>Sky Works</span>
    </div>
  </section>

  <section class="card card-back">
    <div class="green-band"></div>
    <div class="contact-band"></div>

    <div class="identity">
      <p class="person-name">DALTON REYES</p>
      <p class="person-role">Owner</p>
    </div>

    <ul class="contact-list">
      <li><span class="icon"><svg viewBox="0 0 12 12"><path d="M6 0a4 4 0 0 0-4 4c0 3 4 8 4 8s4-5 4-8a4 4 0 0 0-4-4z" fill="#333"/></svg></span>214 W. Elm St.<br>Marlow, OH 45900</li>
      <li><span class="icon"><svg viewBox="0 0 12 12"><path d="M2 1h3l1 3-2 1a7 7 0 0 0 3 3l1-2 3 1v3c-6 0-9-3-9-9z" fill="#333"/></svg></span>419-555-0186</li>
      <li><span class="icon"><svg viewBox="0 0 12 12"><rect x="1" y="2.5" width="10" height="7" fill="#333"/><path d="M1 2.5l5 4 5-4" stroke="#fff" fill="none"/></svg></span>korvaneskyworks@mail.com</li>
      <li><span class="icon"><svg viewBox="0 0 12 12"><circle cx="6" cy="6" r="5" fill="none" stroke="#333" stroke-width="1.5"/><path d="M1 6h10M6 1c-3 3-3 7 0 10M6 1c3 3 3 7 0 10" stroke="#333" fill="none"/></svg></span>www.korvaneskyworks.com</li>
    </ul>

    <ul class="service-list">
      <li>Thermal Image Inspections</li>
      <li>Search &amp; Rescue</li>
      <li>Deer Recovery</li>
      <li>Real Estate Photography</li>
    </ul>

    <div class="back-mark">
      <span class="back-name">Korvane<br>Sky Works</span>
    </div>
  </section>
</body>
</html>
```